Professional banners for an eyewear company

I have 3 images which need to be made into banners. Size 990 x 370, with a 10 pixel white border at top and bottom of banner.

They all need to be adjusted to make the colours better and less bright.
All will need some writing written on them with a nice serif font.

Banner 1 text: Handcrafted luxury eyewear, with a purpose...
Banner 2 text: Half of our profits go to help malnourished children in India
Banner 3 text: 10% of your first order, use code: First Order

On our homepage these 3 banners will alternate, so they need to look good together.

Tips
Please take a look at the banners on the lumentrovic.com homepage, this is kind of how I want the text to be displayed, and they use good colours.

The backgrounds on Banners 2 & 3 can be changed.
Banner 3 background if you can change to a nice colour, as per lumentrovic.com homepage.
Updates

Hi, just a quick update, thank you for all the designs submitted so far, please keep in mind that the brand is a luxury high-end brand so designs will need to reflect this.

Industry/Entity Type

Eyewear

```html
<!DOCTYPE html>
<html lang="en">
<head>
<meta charset="utf-8">
<title>First Order Offer Banner</title>
<link rel="stylesheet" href="https://fonts.googleapis.com/css2?family=Forum&display=swap">
<style>
  :root {
    --border-white: #ffffff;
    --lavender: #c3b9e6;
    --lavender-light: #d0c8ef;
    --lavender-deep: #b2a8dc;
    --disc: rgba(96, 84, 120, 0.42);
    --text: #ffffff;
    --photo-light: #e9e4f3;
    --photo-mid: #b58a72;
    --photo-dark: #6d4a3c;
  }
  * { box-sizing: border-box; margin: 0; padding: 0; }
  html, body {
    width: 1200px;
    height: 448px;
    overflow: hidden;
    background: var(--border-white);
  }
  .banner {
    position: relative;
    width: 1200px;
    height: 448px;
    background: var(--border-white);
    padding: 12px 0;
  }
  .banner__stage {
    position: relative;
    width: 1200px;
    height: 424px;
    overflow: hidden;
  }
  .banner__backdrop {
    position: absolute;
    inset: 0;
    background: linear-gradient(135deg, var(--lavender-light) 0%, var(--lavender) 50%, var(--lavender-deep) 100%);
  }
  .banner__disc {
    position: absolute;
    left: 96px;
    top: 12px;
    width: 400px;
    height: 400px;
    border-radius: 50%;
    background: var(--disc);
  }
  .offer {
    position: absolute;
    left: 0;
    top: 0;
    width: 592px;
    height: 424px;
    color: var(--text);
    font-family: "Forum", "Cormorant Garamond", serif;
    text-transform: uppercase;
    text-align: center;
  }
  .offer__headline {
    position: absolute;
    left: 0;
    right: 0;
    top: 158px;
    font-size: 24px;
    font-weight: 400;
    letter-spacing: 0.5px;
  }
  .offer__code {
    position: absolute;
    left: 0;
    right: 0;
    top: 228px;
    font-size: 36px;
    font-weight: 400;
    letter-spacing: 1px;
  }
  .banner__photo {
    position: absolute;
    left: 703px;
    top: 0;
    width: 412px;
    height: 424px;
    background:
      linear-gradient(180deg, var(--photo-mid) 0%, var(--photo-dark) 30%, var(--photo-light) 62%, var(--photo-light) 100%);
    opacity: 0.9;
  }
</style>
</head>
<body>
  <section class="banner">
    <div class="banner__stage">
      <div class="banner__backdrop" role="img" aria-label="Soft lavender background with a faint triangle pattern"></div>
      <div class="banner__disc"></div>
      <div class="offer">
        <p class="offer__headline">10% of your first order</p>
        <p class="offer__code">Use code: First Order</p>
      </div>
      <div class="banner__photo" role="img" aria-label="Photo of a red-haired model in dark sunglasses and a white polka-dot blouse, looking to the side"></div>
    </div>
  </section>
</body>
</html>
```